Brennock Metal recycling, a business card/logo for our industrial family metal recycling company

A new business card design/logo for our long established family metal recycling company.
I have a logo for our property company which was designed a few months ago on pixel forum which I would like to be very close to this design but have a more industrial feel to it and in a darker blue colour, please see attachments.

Target Market(s)

industries that produce metal waste for recycling, construction sites, engineering companies, manufactures, builders, plumbers, electricians, general house holders.

Industry/Entity Type

Recycling

Contact Information for Business Card

owner/director...Gordon brennock
e-mail....info@brennockscrapworks.example.co.uk
web address.....brennockscrapworks.example.co.uk

Font styles to use
Serif
Sans Serif

Colors
0255a3
ffffff

Requirements
Must have
• -dark blue business card on front.
-white on the back, see contact details, e-mail address for metal company.
-to have an industrial feel to it.
-brennock logo as business card attached but (brennock metal recycling)
please remove the little roof/arrow above brennock as this was relevant to property company.
Nice to have
• please see our website brennockscrapworks.example.co.uk with all details
being correct however I would like to refresh the logo to more like the brennock property investment business card logo attached.
Should not have
• should not contain details from property investments card as this design is for the metal recycling company.

```html
<!DOCTYPE html>
<html lang="en">
<head>
<meta charset="utf-8">
<title>Brennock Metal Recycling — Business Card</title>
<link rel="stylesheet" href="https://fonts.googleapis.com/css2?family=Quicksand:wght@500&family=Montserrat:wght@400&family=Roboto+Condensed:wght@400;700&display=swap">
<style>
  :root {
    --brand-blue: #0255a3;
    --paper-white: #ffffff;
    --backdrop: #dcd7d0;
  }
  html, body {
    margin: 0;
    padding: 0;
    width: 1200px;
    height: 965px;
    overflow: hidden;
    background: var(--backdrop);
  }
  .canvas {
    position: relative;
    width: 1200px;
    height: 965px;
  }
  .card {
    position: absolute;
    left: 278px;
    width: 646px;
    height: 369px;
    border-radius: 26px;
    overflow: hidden;
  }
  .card--front { top: 98px; background: var(--brand-blue); color: var(--paper-white); }
  .card--back  { top: 504px; background: var(--paper-white); color: var(--brand-blue); }

  .wordmark {
    position: absolute;
    left: 0;
    width: 100%;
    text-align: center;
    margin: 0;
    font-family: "Quicksand", sans-serif;
    font-weight: 500;
    color: inherit;
  }
  .wordmark__name {
    display: block;
    font-size: 78px;
    line-height: 1;
    letter-spacing: 4px;
  }
  .wordmark__tagline {
    display: block;
    margin-top: 14px;
    font-size: 18px;
    letter-spacing: 13px;
    padding-left: 13px;
    text-transform: uppercase;
  }
  .card--front .wordmark { top: 132px; }
  .card--back .wordmark  { top: 48px; }

  .contact-person {
    position: absolute;
    left: 20px;
    width: 206px;
    top: 240px;
    text-align: right;
    font-family: "Roboto Condensed", sans-serif;
  }
  .contact-person__name {
    font-weight: 700;
    font-size: 24px;
    line-height: 1;
    margin: 0;
    white-space: nowrap;
    text-transform: uppercase;
  }
  .contact-person__role {
    font-weight: 400;
    font-size: 16px;
    margin: 9px 0 0;
    text-transform: uppercase;
  }
  .contact-divider {
    position: absolute;
    left: 236px;
    top: 229px;
    width: 2px;
    height: 78px;
    background: var(--brand-blue);
  }
  .contact-list {
    position: absolute;
    left: 249px;
    top: 234px;
    margin: 0;
    padding: 0;
    list-style: none;
    font-family: "Montserrat", sans-serif;
    font-size: 14.5px;
    line-height: 23px;
  }
  .contact-list li { display: flex; align-items: center; white-space: nowrap; }
  .contact-list svg { width: 14px; height: 14px; margin-right: 9px; fill: var(--brand-blue); flex: none; }
  .contact-list .contact-list__gap { margin-left: 12px; }
</style>
</head>
<body>
<main class="canvas">
  <section class="card card--front" aria-label="Card front">
    <h1 class="wordmark">
      <span class="wordmark__name">brennock</span>
      <span class="wordmark__tagline">Metal Recycling</span>
    </h1>
  </section>

  <section class="card card--back" aria-label="Card back">
    <h2 class="wordmark">
      <span class="wordmark__name">brennock</span>
      <span class="wordmark__tagline">Metal Recycling</span>
    </h2>

    <div class="contact-person">
      <p class="contact-person__name">Gordon Brennock</p>
      <p class="contact-person__role">Owner-Director</p>
    </div>

    <div class="contact-divider"></div>

    <ul class="contact-list">
      <li>
        <svg viewBox="0 0 24 24" aria-hidden="true"><path d="M6.6 10.8a15 15 0 0 0 6.6 6.6l2.2-2.2c.3-.3.7-.4 1-.2 1.1.4 2.3.6 3.6.6.6 0 1 .4 1 1V20c0 .6-.4 1-1 1A17 17 0 0 1 3 4c0-.6.4-1 1-1h3.5c.6 0 1 .4 1 1 0 1.3.2 2.5.6 3.6.1.3 0 .7-.2 1z"/></svg>
        07700900461
        <svg class="contact-list__gap" viewBox="0 0 24 24" aria-hidden="true"><path d="M7 1h10a2 2 0 0 1 2 2v18a2 2 0 0 1-2 2H7a2 2 0 0 1-2-2V3a2 2 0 0 1 2-2zm0 3v15h10V4zm5 16.2a.9.9 0 1 0 0 1.8.9.9 0 0 0 0-1.8z"/></svg>
        02079460123
      </li>
      <li>
        <svg viewBox="0 0 24 24" aria-hidden="true"><path d="M2 5h20v14H2zm2 2v.5l8 5.5 8-5.5V7zm0 3v7h16v-7l-8 5.5z"/></svg>
        info@brennockscrapworks.example.co.uk
      </li>
      <li>
        <svg viewBox="0 0 24 24" aria-hidden="true"><path d="M12 2a10 10 0 1 0 0 20 10 10 0 0 0 0-20zm-1 17.9A8 8 0 0 1 4.2 10.2L9 15v1a2 2 0 0 0 2 2zm6.9-2.5A2 2 0 0 0 16 16h-1v-3a1 1 0 0 0-1-1H8v-2h2a1 1 0 0 0 1-1V7h2a2 2 0 0 0 2-2v-.4a8 8 0 0 1 2.9 12.8z"/></svg>
        www.brennockscrapworks.example.co.uk
      </li>
    </ul>
  </section>
</main>
</body>
</html>
```